Lanternfield Advisory logo/business card design -- a digital consulting company

I've just restarted a consulting company I had years ago--Lanternfield Advisory. Now I need a new business card and updated logo. The original logo was simple enough: a chart-like progression atop a grid (see the attached file). I do strategy work, and the chart is meant to show incremental growth and profit. I'd like the reincarnation of my logo to be 3D, with both the grid and arrow rotated on their axis.

I'll want to use the logo on my website as well. I'm open to color schemes, fonts, etc.

Target Market(s)

Business-to-Business. Target market is corporate.

Industry/Entity Type

Business

Contact Information for Business Card

Logo on one-side; name and other contact info on the back

Font styles to use
Serif
Sans Serif

Requirements
Nice to have
• Lanternfield Advisory refers to the concept of "bootstrapping" or making incremental changes to grow with minimal risk and financial exposure, and self-sufficiency (think of the phrase "to pull oneself by one's bootstraps.")

```html
<!DOCTYPE html>
<html lang="en">
<head>
<meta charset="utf-8">
<title>Lanternfield Advisory — Business Card</title>
<link rel="stylesheet" href="https://fonts.googleapis.com/css2?family=Kreon:wght@400;600&display=swap">
<style>
  :root {
    --backdrop: #e9e6e1;
    --card-white: #ffffff;
    --brand-indigo: #4557a6;
    --wordmark-indigo: #3f4c9c;
    --link-blue: #3b7fd0;
    --divider: #9aa6d4;
    --text-light: #ffffff;
    --accent-pale: #dfe6fb;
    --accent-sky: #6fb3ee;
  }
  * { box-sizing: border-box; margin: 0; padding: 0; }
  html, body { width: 1000px; height: 1200px; overflow: hidden; }
  body {
    position: relative;
    background: var(--backdrop);
    font-family: "Kreon", Georgia, serif;
  }
  .card {
    position: absolute;
    left: 136px;
    width: 721px;
    height: 420px;
    overflow: hidden;
    box-shadow: 0 2px 8px rgba(0,0,0,0.18);
  }
  .card--front { top: 140px; background: var(--card-white); }
  .card--back  { top: 650px; height: 418px; background: var(--brand-indigo); color: var(--text-light); }

  /* Front */
  .brand-mark {
    position: absolute;
    left: 250px;
    top: 318px;
    width: 22px;
    height: 22px;
    background: var(--wordmark-indigo);
  }
  .brand-mark { top: 178px; left: 268px; }
  .brand-divider {
    position: absolute;
    left: 323px;
    top: 165px;
    width: 1px;
    height: 90px;
    background: var(--divider);
  }
  .wordmark {
    position: absolute;
    left: 348px;
    top: 168px;
    color: var(--wordmark-indigo);
    font-weight: 600;
    font-size: 38px;
    line-height: 40px;
    letter-spacing: 0.5px;
    text-transform: uppercase;
  }
  .front-web {
    position: absolute;
    left: 0;
    right: 0;
    top: 366px;
    text-align: center;
    color: var(--link-blue);
    font-size: 16px;
  }

  /* Back */
  .back-name {
    position: absolute;
    left: 58px;
    top: 46px;
    font-weight: 400;
  }
  .back-name__primary { display: block; font-size: 50px; line-height: 52px; }
  .back-name__secondary { display: block; font-size: 36px; line-height: 40px; }
  .contact-list {
    position: absolute;
    left: 58px;
    top: 292px;
    list-style: none;
    font-size: 18px;
    line-height: 22px;
  }
  .contact-list li { display: flex; align-items: center; gap: 7px; }
  .contact-list svg { width: 14px; height: 14px; fill: var(--text-light); flex: none; }
  .growth-accent {
    position: absolute;
    right: 0;
    bottom: 0;
    width: 300px;
    height: 240px;
  }
</style>
</head>
<body>
  <section class="card card--front" aria-label="Card front">
    <span class="brand-mark" aria-hidden="true"></span>
    <span class="brand-divider" aria-hidden="true"></span>
    <h1 class="wordmark">Lanternfield<br>Advisory</h1>
    <p class="front-web">www.lanternfieldadvisory.com</p>
  </section>

  <section class="card card--back" aria-label="Card back">
    <h2 class="back-name">
      <span class="back-name__primary">Lanternfield</span>
      <span class="back-name__secondary">Advisory</span>
    </h2>
    <ul class="contact-list">
      <li>
        <svg viewBox="0 0 16 16" aria-hidden="true"><path d="M3.6 1.2l2.3 2.6-1.2 1.8c.8 1.9 2.4 3.6 4.4 4.6l1.7-1.3 2.7 2.2-1.5 2.6C6.6 13.3 2.6 9.3 1.2 3.2z"/></svg>
        0140-5521-7308
      </li>
      <li>
        <svg viewBox="0 0 16 16" aria-hidden="true"><path d="M1 3h14v10H1z M1.6 3.6L8 8.8l6.4-5.2" fill="none" stroke="#fff" stroke-width="1.4"/><path d="M1 3h14L8 8.6z"/></svg>
        hello@lanternfieldadvisory.com
      </li>
      <li>
        <svg viewBox="0 0 16 16" aria-hidden="true"><path d="M1 2h14v10H1z M2.4 3.4v7.2h11.2V3.4z M5 13h6v1.4H5z" fill-rule="evenodd"/></svg>
        www.lanternfieldadvisory.com
      </li>
    </ul>
    <svg class="growth-accent" viewBox="0 0 300 240" role="img" aria-label="Growth chart illustration area">
      <defs>
        <linearGradient id="accentFill" x1="0" y1="1" x2="1" y2="0">
          <stop offset="0" stop-color="var(--accent-sky)"/>
          <stop offset="0.55" stop-color="var(--accent-pale)"/>
          <stop offset="1" stop-color="#ffffff"/>
        </linearGradient>
      </defs>
      <polygon points="0,240 300,0 300,240" fill="url(#accentFill)"/>
    </svg>
  </section>
</body>
</html>
```